SKYWARD LENSWORKS New Wordpress Design Project

Skyward Lensworks is a photo-sharing site for aviation photographers and enthusiasts.

Please redesign the home page (http://www.skywardlensworks.example/) and photo feature page (http://www.skywardlensworks.example/2014/10/borvel-freight-23/).

We like and would like to keep the logo we have, but are open to changing colors on the logo to suit a new color scheme if necessary.
Updates

Hi All, Thank you for taking part in this design competition. Could you please show us your first round design concepts within 24hrs as we hope to show our client them and start providing feedback? Much appreciated, Lex VH BramblePeak Design

Hi All, A few tips: Could you try keep the search bar above the fold Include a section for showing new blog posts Try to integrate an ads a little better also above and below the fold Appreciated, Lex Vh

Target Market(s)

Aviation photographers and enthusiasts of all age groups globally.

Industry/Entity Type

Aviation

Requirements
Must have
• • Clean and consistent layout
• A good way to incorporate advertisements on the home page and photo feature page
• Clear and simple menu navigation
• On home page – call to action to register
• On home page - call to action to upload photos
• On home page – social buttons call to action to follow, circle, like, etc
• On photo feature page – call to action to tweet, +1, Like, etc a photo
Nice to have
• Sites we like

www.quillpane.example
http://www.layoutorchard.example/demo/45176.html
Should not have
• • Unnecessary animations
• No Adobe Flash
• Overly crowded / busy design

```html
<!DOCTYPE html>
<html lang="en">
<head>
<meta charset="utf-8">
<title>Skyward Lensworks</title>
<link href="https://fonts.googleapis.com/css2?family=Open+Sans:wght@400;600;700&display=swap" rel="stylesheet">
<style>
:root{
  --orange:#f07b12;
  --orange-dark:#d9650a;
  --text:#555;
  --heading-orange:#ee7c1c;
  --light:#ececec;
  --white:#fff;
  --footer:#2e2e2e;
  --footer-text:#bdbdbd;
  --ad-blue:#1c6fb8;
  --nav:#666;
}
*{box-sizing:border-box;margin:0;padding:0}
html,body{width:741px;height:1200px;overflow:hidden}
body{font-family:"Open Sans",Arial,sans-serif;color:var(--text);background:var(--white);position:relative}

.site-header{height:69px;display:flex;align-items:center;padding:0 20px 0 28px;justify-content:space-between}
.brand{font-size:22px;font-weight:700;color:#2b2b2b;letter-spacing:-.3px}
.header-right{display:flex;flex-direction:column;align-items:flex-end;gap:8px}
.social{display:flex;gap:10px}
.social span{width:12px;height:12px;border-radius:50%;background:#8a8a8a;display:block}
.main-nav{display:flex;gap:0;font-size:10.5px}
.main-nav a{color:var(--nav);text-decoration:none;padding:4px 10px}
.main-nav a.active{background:#f3f3f3;color:var(--orange);border-bottom:2px solid var(--orange)}

.hero{position:relative;height:340px;background:linear-gradient(180deg,#cfd7df 0%,#dfe3e6 35%,#4f6a3f 36%,#6f8455 60%,#7d7f80 72%,#9a9c9b 100%)}
.hero .plane{position:absolute;inset:0}
.hero-arrow{position:absolute;top:135px;width:26px;height:26px;border-radius:50%;background:rgba(0,0,0,.45);display:flex;align-items:center;justify-content:center}
.hero-arrow.left{left:12px}.hero-arrow.right{right:12px}
.search-bar{position:absolute;left:0;right:0;bottom:0;height:30px;background:var(--orange);display:flex;align-items:center;padding:0 12px 0 65px;justify-content:space-between}
.search-bar span{color:#fff;font-size:10px;font-style:normal}
.search-btn{width:18px;height:18px;border-radius:50%;background:#3a3a3a;display:flex;align-items:center;justify-content:center}

.welcome{text-align:center;padding:18px 150px 0}
.welcome h1{font-size:19px;font-weight:600;color:var(--heading-orange);margin-bottom:10px}
.welcome p{font-size:9.5px;line-height:1.55;color:#777}
.btn{display:inline-block;background:var(--orange);color:#fff;font-size:9.5px;font-weight:700;padding:6px 18px;border-radius:2px;margin-top:16px;letter-spacing:.3px}

.gallery{position:absolute;top:585px;left:0;width:741px;height:305px;background:var(--light)}
.tabs{display:flex;justify-content:center;margin-top:28px}
.tabs span{font-size:9.5px;padding:5px 16px;background:#fff;border:1px solid #d6d6d6;color:#777}
.tabs span.active{background:#444;color:#fff;border-color:#444}
.grid{display:grid;grid-template-columns:repeat(4,140px);gap:20px 18px;justify-content:center;margin-top:20px}
.thumb{height:86px;border:3px solid #fff;box-shadow:0 1px 2px rgba(0,0,0,.15)}
.t1{background:linear-gradient(180deg,#b9c8d6 55%,#7e8a72)}
.t2{background:linear-gradient(180deg,#6fa1d8,#d6e4f1)}
.t3{background:linear-gradient(180deg,#c9cdd0 50%,#8e9270)}
.t4{background:linear-gradient(180deg,#dfe6ec 55%,#9aa19e)}
.t5{background:linear-gradient(180deg,#7fa7cf 55%,#7c7a70)}
.t6{background:linear-gradient(180deg,#a8b7c2 55%,#5d6b55)}
.t7{background:linear-gradient(180deg,#d3d9de 55%,#8f928c)}
.t8{background:linear-gradient(180deg,#9fc1e1 55%,#727a82)}

.ads{position:absolute;top:900px;left:74px;width:606px;display:flex;gap:25px}
.ad{height:42px;flex:1;border:1px solid #c9d7e6;background:#f4f8fc;display:flex;align-items:center;justify-content:space-between;padding:0 10px;font-size:9px;color:var(--ad-blue)}
.ad strong{font-size:11px;display:block;color:#14528c}
.ad .go{width:22px;height:22px;background:#22313f;display:flex;align-items:center;justify-content:center;border-radius:2px}
.ad .deal{background:var(--ad-blue);color:#fff;padding:4px 8px;font-weight:700;font-size:9px}

.upload{position:absolute;top:990px;left:0;width:741px;text-align:center;padding:0 170px}
.upload h2{font-size:19px;font-weight:600;color:var(--heading-orange);margin-bottom:8px}
.upload p{font-size:9.5px;line-height:1.55;color:#777}
.upload .btn{margin-top:12px}

.site-footer{position:absolute;left:0;top:1110px;width:741px;height:90px;background:var(--footer);color:var(--footer-text)}
.footer-nav{display:flex;justify-content:center;gap:22px;font-size:9px;margin-top:24px}
.footer-bottom{display:flex;justify-content:space-between;align-items:center;padding:0 20px;margin-top:24px;font-size:8.5px}
.footer-bottom .social span{background:#7a7a7a}
</style>
</head>
<body>
<header class="site-header">
  <div class="brand">Skyward Lensworks</div>
  <div class="header-right">
    <div class="social"><span></span><span></span><span></span></div>
    <nav class="main-nav">
      <a class="active">Home</a><a>Photos</a><a>Submit a Photo</a><a>Airport Search</a><a>Login</a><a>Register</a>
    </nav>
  </div>
</header>

<section class="hero">
  <div class="plane" role="img" aria-label="Featured photo of a colourful passenger jet taxiing on an airport apron"></div>
  <div class="hero-arrow left"><svg width="10" height="10" viewBox="0 0 10 10"><path d="M7 1 3 5l4 4" stroke="#fff" stroke-width="2" fill="none"/></svg></div>
  <div class="hero-arrow right"><svg width="10" height="10" viewBox="0 0 10 10"><path d="M3 1l4 4-4 4" stroke="#fff" stroke-width="2" fill="none"/></svg></div>
  <div class="search-bar">
    <span>Enter a search query here...</span>
    <div class="search-btn"><svg width="10" height="10" viewBox="0 0 10 10"><circle cx="4" cy="4" r="3" stroke="#fff" stroke-width="1.5" fill="none"/><path d="M6.3 6.3 9 9" stroke="#fff" stroke-width="1.5"/></svg></div>
  </div>
</section>

<section class="welcome">
  <h1>Welcome to Skyward Lensworks</h1>
  <p>Nullam nec convallis nisl. Donec hendrerit dui dolor, nunc quis purus convallis, semper arcu quam lectus sed augue. Cras quis nisi a ex auctor mattis. Ut sapien nisi vestibulum ac tempus, vitae pellentesque laoreet a mi amet nunc. Donec imperdiet sodales dignissim. Duis feugiat nisi sit amet magna luctus, non ultrices turpis rhoncus.</p>
  <span class="btn">REGISTER NOW</span>
</section>

<section class="gallery">
  <div class="tabs"><span class="active">Top Photos</span><span>Most Viewed Today</span><span>Most Viewed - All Time</span></div>
  <div class="grid">
    <div class="thumb t1" role="img" aria-label="Airliner on the runway"></div>
    <div class="thumb t2" role="img" aria-label="Business jet in flight"></div>
    <div class="thumb t3" role="img" aria-label="Airliner taking off"></div>
    <div class="thumb t4" role="img" aria-label="Airliner taxiing"></div>
    <div class="thumb t5" role="img" aria-label="Airliner on the apron"></div>
    <div class="thumb t6" role="img" aria-label="Jet landing"></div>
    <div class="thumb t7" role="img" aria-label="Airliner parked at gate"></div>
    <div class="thumb t8" role="img" aria-label="Airliner on approach"></div>
  </div>
</section>

<section class="ads">
  <div class="ad"><div><strong>Veyra Travel</strong>Compare fares on every route</div><div class="go"><svg width="8" height="8" viewBox="0 0 8 8"><path d="M2 1l4 3-4 3" stroke="#fff" stroke-width="1.5" fill="none"/></svg></div></div>
  <div class="ad"><div><strong>Summer seat sale</strong>up to 40% off</div><span class="deal">Book now</span><strong>Harbor Tickets</strong></div>
</section>

<section class="upload">
  <h2>Nullam nec convallis</h2>
  <p>Donec imperdiet sodales dignissim. Duis feugiat nisi sit amet magna luctus, non ultrices turpis rhoncus. Etiam vestibulum, leo quis eleifend pulvinar, dui ante semper velit, vel posuere nunc purus vel nunc.</p>
  <span class="btn">UPLOAD PHOTOS</span>
</section>

<footer class="site-footer">
  <nav class="footer-nav"><span>Home</span><span>Photos</span><span>Submit a Photo</span><span>Airport Search</span><span>Login</span><span>Register</span></nav>
  <div class="footer-bottom">
    <span>Copyright © 2014 Skyward Lensworks. All rights reserved.</span>
    <div class="social"><span></span><span></span><span></span></div>
  </div>
</footer>
</body>
</html>
```